Supplement Label Design for “Kelvora Gut” – Premium Bilingual Supplement

Kelvora is a premium, individually crafted supplement brand specializing in targeted solutions for specific health issues.
We are launching our first product: Kelvora Gut — a high-quality blend focused on stomach and digestive health.
Primary goals:
• Reduce symptoms caused by Helicobacter pylori (acidity after meals, stomach pain and discomfort)
• Support repair of the gut lining
• Strengthen the local immune system in the digestive tract
Label Requirements:
• Premium, elegant, and modern design (high-end supplement feel)
• Dominant yellow / golden color scheme for this Gut blend (future blends will have different signature colors, e.g. red for Heart blend)
• Include a stylized, positive illustration of a healthy stomach on the label
• Fully bilingual — English and Bulgarian if possible (both languages must be clearly visible and well balanced)
• Logo is already uploaded
• Must feel trustworthy, clean, and professional
We need both front and back label designs suitable for a standard supplement bottle.

Target Market(s)

The target is health-conscious individuals, particularly my personal patients who suffer from stomach issues, H. pylori related symptoms, and digestive discomfort. People looking for premium, science-oriented natural supplements.

Industry/Entity Type

Functional medicine

Font styles to use
Sans Serif

Colors
FFC000
F8CF3A
FAE287
FDF2CF
FEFAEE

Requirements
Must have
• • Premium and luxurious look • Dominant yellow/golden color palette • Stylized healthy stomach illustration • Bilingual (English + Bulgarian) • Clean, minimalist yet elegant design • Professional and trustworthy appearance • Include the “Kelvora” logo
Nice to have
• • Subtle visual indication of positive effect on the stomach/gut • Elegant iconography or subtle patterns related to health and nature • Easy-to-read hierarchy for important information • Modern minimalist style with premium finishing feel
Should not have
• Cheap or generic look • Overly cartoonish or childish stomach drawing • Too much clutter or overcrowded desig

```html
<!DOCTYPE html>
<html lang="en">
<head>
<meta charset="utf-8">
<title>Kelvora Gut – Label Set</title>
<link href="https://fonts.googleapis.com/css2?family=Cinzel:wght@500;700&family=Roboto:wght@400;500;700&family=Roboto+Condensed:wght@400;500&display=swap" rel="stylesheet">
<style>
  :root{
    --canvas:#ececec;
    --white:#ffffff;
    --cream:#fdf2cf;
    --ivory:#fefaee;
    --butter:#fae287;
    --sun:#f8cf3a;
    --amber:#ffc000;
    --gold:#d4a017;
    --gold-deep:#b7860b;
    --green:#0f7a3c;
    --ink:#2b2b2b;
    --grey:#5a5a5a;
    --rule:#c9a23a;
  }
  *{box-sizing:border-box;margin:0;padding:0}
  html,body{width:1200px;height:630px;overflow:hidden;background:var(--canvas)}
  .canvas{position:relative;width:1200px;height:630px;display:flex;justify-content:center;align-items:center;gap:48px}

  .label{position:relative;width:296px;height:614px;background:var(--white);overflow:hidden;font-family:"Roboto",sans-serif;color:var(--ink)}

  /* front */
  .front-decor{position:absolute;inset:0}
  .brand-mark{position:absolute;top:38px;left:0;right:0;text-align:center;font-family:"Cinzel",serif;font-weight:500;font-size:20px;letter-spacing:1px;color:var(--gold)}
  .brand-mark .dot{display:inline-block;width:6px;height:6px;border-radius:50%;background:var(--gold);vertical-align:middle;margin-right:6px}
  .product-line{position:absolute;top:82px;left:0;right:0;text-align:center;font-family:"Cinzel",serif;font-weight:700;font-size:23px;color:var(--green);letter-spacing:.5px}
  .product-name{position:absolute;top:104px;left:0;right:0;text-align:center;font-family:"Cinzel",serif;font-weight:700;font-size:60px;line-height:1;
    background:linear-gradient(180deg,#f3c94a 0%,#d4a017 55%,#a87708 100%);-webkit-background-clip:text;background-clip:text;color:transparent}
  .front-desc{position:absolute;left:40px;right:40px;text-align:center;font-size:6.6px;line-height:1.55;color:var(--grey)}
  .front-desc.en{top:172px}
  .front-desc.bg{top:455px}
  .stomach-art{position:absolute;left:38px;top:235px;width:222px;height:180px;border-radius:50%;
    background:radial-gradient(ellipse at 50% 48%,#fff4c4 0%,#f8cf3a 32%,#e3a91a 55%,rgba(250,226,135,.45) 75%,rgba(253,242,207,0) 100%)}
  .product-name-bg{position:absolute;top:414px;left:0;right:0;text-align:center;font-weight:700;font-size:27px;color:var(--green);letter-spacing:.3px}

  .benefits{position:absolute;left:8px;right:8px;top:528px;display:flex;justify-content:space-between}
  .benefit{width:68px;text-align:center;color:var(--white)}
  .benefit-icon{width:30px;height:30px;margin:0 auto;border-radius:50%;background:var(--white);border:2px solid var(--butter);display:flex;align-items:center;justify-content:center}
  .benefit-en{margin-top:6px;font-size:5.2px;font-weight:500;letter-spacing:.1px}
  .benefit-rule{width:16px;height:1px;background:var(--green);margin:4px auto}
  .benefit-bg{font-size:5.2px;font-weight:500;line-height:1.4}

  .front-footer{position:absolute;left:0;right:0;bottom:0;height:24px;background:var(--green);color:var(--white);display:flex;align-items:center;justify-content:space-between;padding:0 10px;font-size:6px}
  .front-footer b{font-family:"Cinzel",serif;font-weight:700;font-size:7px;letter-spacing:.3px}

  /* back */
  .back{padding:14px 9px 0 9px;font-family:"Roboto Condensed",sans-serif}
  .back-corner{position:absolute;top:0;left:0;right:0;height:30px}
  .back h2{font-family:"Roboto",sans-serif;font-weight:500;font-size:9.5px;color:var(--ink);margin-bottom:4px;position:relative}
  .back p.small{font-size:4.9px;line-height:2.1;color:var(--grey);margin-bottom:6px;text-align:justify}
  .comp-table{width:260px;margin:4px auto 10px;border-collapse:collapse;border:1px solid var(--rule);font-size:6px;color:var(--grey)}
  .comp-table th{background:var(--cream);font-family:"Cinzel",serif;font-weight:500;font-size:7px;color:var(--gold-deep);text-align:left;padding:4px 6px;line-height:1.3;border-right:1px solid var(--rule)}
  .comp-table th.num{text-align:center}
  .comp-table th .sub{font-family:"Roboto Condensed",sans-serif;color:var(--ink);font-size:6.5px}
  .comp-table td{padding:4px 6px;line-height:1.5;border-top:1px solid #d9d2bd;border-right:1px solid var(--rule)}
  .comp-table td.num{text-align:center}
  .two-col{display:flex;gap:14px;margin-bottom:6px}
  .two-col > div{flex:1}
  .two-col h3{font-family:"Roboto",sans-serif;font-weight:500;font-size:6.8px;margin-bottom:4px}
  .two-col p{font-size:5.4px;line-height:1.6;color:var(--grey)}
  .dosage{margin:0 -9px 8px;background:var(--cream);padding:6px 9px;text-align:center;font-size:5.2px;line-height:1.8;color:var(--gold-deep)}
  .dosage b{color:var(--ink);font-weight:500}
  .back h4{font-family:"Roboto",sans-serif;font-weight:500;font-size:6.8px;margin-bottom:3px}
  .back p.tiny{font-size:4.1px;line-height:1.6;color:var(--grey);text-align:justify;margin-bottom:6px}
  .parties{display:flex;gap:14px}
  .parties > div{flex:1}
  .parties p{font-size:3.6px;line-height:1.6;color:var(--grey)}
  .back-footer{position:absolute;left:0;right:0;bottom:0;height:16px;background:var(--green);color:var(--white);display:flex;align-items:center;padding:0 11px;font-size:6px;font-weight:500;font-family:"Roboto",sans-serif}
  .back-footer span:last-child{margin-left:auto;margin-right:56px}
</style>
</head>
<body>
<main class="canvas">

  <!-- FRONT LABEL -->
  <section class="label front" aria-label="Kelvora Gut front label">
    <svg class="front-decor" width="296" height="614" viewBox="0 0 296 614" aria-hidden="true">
      <defs>
        <linearGradient id="creamWave" x1="0" y1="0" x2="0" y2="1">
          <stop offset="0" stop-color="#fefaee"/>
          <stop offset="1" stop-color="#fdf2cf"/>
        </linearGradient>
        <linearGradient id="goldBand" x1="0" y1="0" x2="0" y2="1">
          <stop offset="0" stop-color="#f4d160"/>
          <stop offset="1" stop-color="#d9a514"/>
        </linearGradient>
      </defs>
      <rect x="0" y="0" width="296" height="3" fill="#e0b23a"/>
      <path d="M0 0 H32 C16 18 6 40 0 68 Z" fill="#e7bf4a"/>
      <path d="M0 66 C6 40 18 16 30 0 H22 C12 16 4 36 0 56 Z" fill="var(--green)"/>
      <path d="M0 290 C70 220 180 230 296 140 V520 H0 Z" fill="url(#creamWave)"/>
      <path d="M0 292 C70 222 180 232 296 142" stroke="#e2b73f" stroke-width="1.5" fill="none"/>
      <path d="M0 520 C90 492 200 530 296 498 V614 H0 Z" fill="url(#goldBand)"/>
    </svg>

    <div class="brand-mark"><span class="dot"></span>Kelvora</div>
    <div class="product-line">KELVORA</div>
    <div class="product-name">GUT</div>
    <p class="front-desc en">Food supplement with vegetable extracts of Licorice, Red elm, Althaea, Aloe vera, with Mastics of Chios, N-acetylcysteine and Lactoferrin.</p>

    <div class="stomach-art" role="img" aria-label="Glowing golden illustration of a healthy stomach surrounded by light rings"></div>

    <div class="product-name-bg">КЕЛВОРА ГЪТ</div>
    <p class="front-desc bg">Хранителна добавка с растителни екстракти от Женско биле, Червен бряст, Алтея, Алое вера, с Мастика от Хиос, N-ацетилцистеин и Лактоферин.</p>

    <div class="benefits">
      <div class="benefit">
        <div class="benefit-icon"><svg width="14" height="14" viewBox="0 0 14 14"><circle cx="7" cy="7" r="5" fill="none" stroke="var(--green)" stroke-width="1.4"/><path d="M4.5 7.2l1.7 1.7 3.4-3.6" fill="none" stroke="var(--green)" stroke-width="1.4"/></svg></div>
        <div class="benefit-en">DIGESTIVE COMFORT</div><div class="benefit-rule"></div>
        <div class="benefit-bg">КОМФОРТ ПРИ ХРАНОСМИЛАНЕ</div>
      </div>
      <div class="benefit">
        <div class="benefit-icon"><svg width="14" height="14" viewBox="0 0 14 14"><path d="M7 1.5l4.5 1.8v3.4c0 3-2 4.8-4.5 5.8-2.5-1-4.5-2.8-4.5-5.8V3.3z" fill="none" stroke="var(--green)" stroke-width="1.3"/></svg></div>
        <div class="benefit-en">GUT LINING SUPPORT</div><div class="benefit-rule"></div>
        <div class="benefit-bg">ПОДПОМАГА ЛИГАВИЦАТА</div>
      </div>
      <div class="benefit">
        <div class="benefit-icon"><svg width="14" height="14" viewBox="0 0 14 14"><circle cx="7" cy="7" r="2" fill="var(--green)"/><circle cx="2.5" cy="3" r="1.2" fill="var(--green)"/><circle cx="11.5" cy="3" r="1.2" fill="var(--green)"/><circle cx="2.5" cy="11" r="1.2" fill="var(--green)"/><circle cx="11.5" cy="11" r="1.2" fill="var(--green)"/><path d="M3 3.5L7 7l4-3.5M3 10.5L7 7l4 3.5" stroke="var(--green)" stroke-width=".8" fill="none"/></svg></div>
        <div class="benefit-en">IMMUNE SUPPORT</div><div class="benefit-rule"></div>
        <div class="benefit-bg">ПОДКРЕПА НА ИМУНИТЕТА</div>
      </div>
      <div class="benefit">
        <div class="benefit-icon"><svg width="14" height="14" viewBox="0 0 14 14"><path d="M7 12.5V6M7 8C4 8 3 5.5 3 3.5c2.5 0 4 1.5 4 4.5zM7 7c0-3 1.5-4.5 4-4.5 0 2-1 4.5-4 4.5z" fill="none" stroke="var(--green)" stroke-width="1.1"/></svg></div>
        <div class="benefit-en">NATURAL INGREDIENTS</div><div class="benefit-rule"></div>
        <div class="benefit-bg">НАТУРАЛНИ СЪСТАВКИ</div>
      </div>
    </div>

    <footer class="front-footer">
      <span><b>DIETARY SUPPLEMENT</b> &nbsp;|&nbsp; ХРАНИТЕЛНА ДОБАВКА</span>
      <span><b>60 CAPSULES</b> | КАПСУЛИ</span>
    </footer>
  </section>

  <!-- BACK LABEL -->
  <section class="label back" aria-label="Kelvora Gut back label">
    <svg class="back-corner" width="296" height="30" viewBox="0 0 296 30" aria-hidden="true">
      <rect x="0" y="0" width="296" height="3" fill="#e0b23a"/>
      <path d="M268 0 H296 V30 C288 16 280 6 268 0 Z" fill="#e7bf4a"/>
      <path d="M276 0 C286 8 292 18 296 30 V22 C292 12 286 4 282 0 Z" fill="var(--green)"/>
    </svg>

    <h2>COMPOSITION:</h2>
    <p class="small">Chios mastica (Pistacia lentinus L., gum-resin; carrier: corn maltodextrin); capsule [hidroxypropylmethylcellulose]; licorice deglycyrrhizinated d.e. 1:4 (Glycyrrhiza glabra L., radix; carrier: corn maltodextrin); aloe vera gel 200:1 (Aloe vera (L.) Burm.f., gelum sine cute); N-acetylcysteine; Red elm d.e.10:1 (Ulmus rubra Muhl, cortex); Althaea d.e. 1:4 (Althaea officinalis L., radix; carrier: corn maltodextrin); Lactoferrin 95% (milk and product thereof - including lactose); corn maltodextrin; anticaking agent: silicon dioxide</p>

    <h2>СЪСТАВ:</h2>
    <p class="small">Мастика от Хиос (Pistacia lentinus L., гумена смола; носител: царевичен малтодекстрин); капсула [хидроксипропилметилцелулоза]; деглициризирано женско биле 1:4 (Glycyrrhiza glabra L., корен; царевичен малтодекстрин); гел от алое вера 200:1 (Aloe vera (L.) Burm.f., gelum sine cute); N-ацетилцистеин; червен бряст 10:1 (Ulmus rubra Muhl, кора; алтея 1:4 (Althaea officinalis L., корен; царевичен малтодекстрин)); Лактоферин 95% (мляко и продукти от него - включително лактоза); царевичен малтодекстрин; агент против слепване: силициев диоксид.</p>

    <table class="comp-table">
      <thead>
        <tr><th>COMPONENTS<br><span class="sub">СЪСТАВКИ</span></th><th class="num">PER CPS<br><span class="sub">ЗА 1 капсула</span></th><th class="num">PER 3 CPS<br><span class="sub">За 3 капсули</span></th></tr>
      </thead>
      <tbody>
        <tr><td>Chios Mastica<br>Мастика от Хиос</td><td class="num">320 mg<br>320 мг</td><td class="num">960 mg<br>960 мг</td></tr>
        <tr><td>Licorice deglycyrrhizinated d.e<br>Женско биле с.е.</td><td class="num">80 mg<br>80 мг</td><td class="num">240 mg<br>240 мг</td></tr>
        <tr><td>Aloe vera d.e.<br>Алое вера с.е.</td><td class="num">50 mg<br>50 мг</td><td class="num">150 mg<br>150 мг</td></tr>
        <tr><td>N-acetylcysteine<br>N-ацетилцистеин</td><td class="num">40 mg<br>40 мг</td><td class="num">120 mg<br>120 мг</td></tr>
        <tr><td>Red elm d.e.<br>Червен бряст с.е.</td><td class="num">40 mg<br>40 мг</td><td class="num">120 mg<br>120 мг</td></tr>
        <tr><td>Althaea d.e.<br>Алтея с.е.</td><td class="num">40 mg<br>40 мг</td><td class="num">120 mg<br>120 мг</td></tr>
        <tr><td>Lactoferrin<br>Лактоферин</td><td class="num">30 mg<br>30 мг</td><td class="num">90 mg<br>90 мг</td></tr>
      </tbody>
    </table>

    <div class="two-col">
      <div><h3>PHYSIOLOGICAL VALUES:</h3><p>Pistacia lentiscus and Licorice supports digestive system function.</p></div>
      <div><h3>ФИЗИОЛОГИЧНИ СТОЙНОСТИ:</h3><p>Мастиката и женското биле подпомагат функцията на храносмилателната система.</p></div>
    </div>

    <div class="dosage">
      <b>RECOMMENDED DAILY DOSAGE:</b> It is recommended to take up to three capsules per day.<br>
      <b>ПРЕПОРЪЧИТЕЛНА ДНЕВНА ДОЗА:</b> Препоръчва се прием до три капсули на ден.
    </div>

    <h4>STORAGE CONDITIONS:</h4>
    <p class="tiny">Store in a cool (&lt;25°C), dry place away from sources of light and heat. RECOMMENDATIONS: Keep out of reach of children. Food supplements are not intended as a substitute for a varied and balanced diet and a healthy lifestyle. Do not exceed the recommended daily dose. The expiration date refers to the product in its intact packaging and stored correctly. SPECIAL INSTRUCTIONS: Do not give to children under 12 years of age. Consult your doctor if you are pregnant or breastfeeding.</p>

    <h4>УСЛОВИЯ НА СЪХРАНЕНИЕ:</h4>
    <p class="tiny">Съхранявайте на хладно (&lt;25°C), сухо място, далеч от източници на светлина и топлина. ПРЕПОРЪКИ: Да се съхранява на място, недостъпно за деца. Хранителните добавки не са предназначени като заместител на разнообразното и балансирано хранене. Не превишавайте препоръчителната дневна доза. СПЕЦИАЛНИ ИНСТРУКЦИИ: Да не се дава на деца под 12-годишна възраст.</p>

    <div class="parties">
      <div><h4>MANUFACTURER/ПРОИЗВОДИТЕЛ:</h4><p>Lumeria Farmaceutici – via Olmo 8, 40100 Bologna – Italy /<br>Лумерия Фармачеутичи – виа Олмо 8, 40100 Болоня</p></div>
      <div><h4>DISTRIBUTOR/ДИСТРИБУТОР:</h4><p>Sarvo Distribution – registered office address and phone<br>Сарво Дистрибюшън – адрес на управление и телефон</p></div>
    </div>

    <footer class="back-footer"><span>Lotto: Партида</span><span>Scadenza:Срок на годност:</span></footer>
  </section>

</main>
</body>
</html>
```